Ceramic worktop for laboratory furniture

We want a simple product catalog, maybe 4-8 pages, our ceramic worktop was chemical resistant, is a good worktop material for high chemicals corrosion environment like laboratory furniture, fumecupboard.

You can visit http://www.glazebenchsurface.com/products/PELM%20BENCH%20SURFACE%20PAIRED%20ITEMS.html
https://www.clipmesh.example/731902846551207/videos/6048215379012764/?__so__=channel_tab&__rv__=all_videos_card

http://www.benchora-gulf.example/products/lab-furniture-series/worktops#verticalTab3

https://www.quillbrookfitouts.example/blog/laboratory-countertop-material/

https://resources.tarnvalefabrication.example/blog/top-5-materials-to-consider-for-your-lab-countertops

https://www.morvik.example/blog/type-of-laboratory-worktops-their-selection-criteria/

https://www.brenholt.example/Brenholt/Literature/Blog/The-Different-Laboratory-Worksurfaces.htm

as reference

Target Market(s)

Asia, UAE and India

Industry/Entity Type

Laboratory fumecupboard and laboratory furniture manufacturer

Font styles to use
Sans Serif

Colors
00AB8E
00BBA5
67D7C9
C6EFE9
E9F9F6

Requirements
Must have
• This catalog mainly will sent to my customer handphone

```html
<!DOCTYPE html>
<html lang="en">
<head>
<meta charset="utf-8">
<title>Verdant Lab – Ceramic Worktop Catalogue</title>
<link href="https://fonts.googleapis.com/css2?family=Montserrat:wght@300;400;500;600;700;800&display=swap" rel="stylesheet">
<style>
  :root{
    --stage:#f2f2f2;
    --paper:#ffffff;
    --paper-grey:#e4e4e4;
    --ink:#1e1f21;
    --ink-soft:#4a4c4f;
    --dark-panel:#2b2d30;
    --green:#2fae3e;
    --orange:#e2531c;
    --photo-light:#d9dde1;
    --photo-mid:#aeb5bb;
    --white:#ffffff;
  }
  *{box-sizing:border-box;margin:0;padding:0}
  html,body{width:825px;height:1200px;overflow:hidden}
  body{background:var(--stage);font-family:"Montserrat",sans-serif;color:var(--ink);position:relative}
  .spread{position:absolute;left:52px;width:720px;height:500px;display:flex;box-shadow:0 6px 24px rgba(0,0,0,.12)}
  .spread--outer{top:60px}
  .spread--inner{top:640px}
  .page{position:relative;width:360px;height:500px;overflow:hidden;background:var(--paper)}
  .page + .page{border-left:1px solid #d4d4d4}
  .page__bg{position:absolute;inset:0;width:100%;height:100%}
  .brand{font-weight:800;font-size:17px;color:var(--ink);display:flex;align-items:center;gap:6px;letter-spacing:-.2px}
  .brand__mark{width:12px;height:12px;background:var(--green)}
  .brand--small{font-size:11px}
  .brand--small .brand__mark{width:8px;height:8px}

  /* back cover */
  .about{position:absolute;left:30px;top:28px;right:24px;color:var(--white)}
  .about__title{font-weight:800;font-size:16px;margin-bottom:6px}
  .about__rule{height:1px;background:rgba(255,255,255,.7);margin-bottom:10px}
  .about__cols{display:flex;gap:14px}
  .about__col p{font-size:5.6px;line-height:1.5;margin-bottom:5px;color:#e8e8e8}
  .contact__title{position:absolute;left:30px;top:282px;color:var(--white);font-weight:800;font-size:16px}
  .contact__company{position:absolute;left:30px;top:372px;font-weight:700;font-size:9px}
  .contact__address{position:absolute;left:30px;top:390px;font-size:8px;font-weight:600;line-height:1.35;width:160px}
  .contact__address svg{vertical-align:-1px;margin-right:3px}
  .contact__logo{position:absolute;right:30px;top:388px}
  .contact__lines{position:absolute;right:30px;top:440px;list-style:none;font-size:8px;font-weight:600;line-height:1.6}
  .contact__lines svg{vertical-align:-1px;margin-right:4px}

  /* front cover */
  .cover__title{position:absolute;left:42px;top:300px;color:var(--white);border-left:2px solid var(--white);padding-left:10px}
  .cover__light{font-weight:300;font-size:20px;line-height:1.05;display:block}
  .cover__bold{font-weight:800;font-size:22px;line-height:1.05;display:block}
  .cover__sub{font-weight:700;font-size:13px;display:block;margin-top:6px}
  .cover__web{position:absolute;left:30px;top:420px;font-size:9px;font-weight:600;letter-spacing:1px}
  .cover__web b{color:var(--green)}
  .cover__logo{position:absolute;right:30px;top:456px}

  /* inside left */
  .product__band{position:absolute;left:0;top:0;width:100%;height:92px;background:var(--orange);color:var(--white);padding:26px 0 0 34px}
  .product__band-inner{border-left:2px solid var(--white);padding-left:9px}
  .product__code{font-size:10px;font-weight:500;display:block}
  .product__name{font-size:13px;font-weight:800;letter-spacing:.4px;display:block}
  .features{position:absolute;left:22px;top:108px;width:316px;display:grid;grid-template-columns:repeat(4,1fr);row-gap:10px;list-style:none}
  .feature{text-align:center;font-size:7px;font-weight:600;line-height:1.2}
  .feature__icon{display:block;margin:0 auto 4px;width:34px;height:34px}
  .swatches{position:absolute;left:22px;top:268px;display:flex;gap:10px}
  .swatch{display:flex;align-items:stretch;height:58px}
  .swatch__tab{width:16px;background:var(--orange);color:var(--white);font-size:7px;font-weight:700;writing-mode:vertical-rl;transform:rotate(180deg);text-align:center}
  .swatch__chip{width:80px;border:1px solid #bdbdbd}
  .swatch__chip--white{background:#ffffff}
  .swatch__chip--grey{background:#a8a8a8}
  .swatch__chip--black{background:#111}
  .size-bar{position:absolute;left:22px;top:338px;width:316px;height:26px;background:var(--green);color:var(--white);font-weight:600;font-size:11px;letter-spacing:.6px;display:flex;align-items:center;justify-content:center}
  .product__text{position:absolute;left:22px;top:374px;width:316px;font-size:6.4px;line-height:1.55;color:var(--ink-soft)}
  .footer{position:absolute;left:22px;right:22px;bottom:20px;display:flex;align-items:center;gap:8px}
  .footer__web{font-size:7px;font-weight:600}
  .footer__web b{color:var(--green)}
  .footer__rule{flex:1;height:1px;background:#888}

  /* inside right */
  .gallery__photo{position:absolute;left:22px;width:316px}
  .gallery__photo--white{top:30px;height:190px;background:linear-gradient(135deg,#e8ebee 0%,#c9ced3 60%,#dfe3e6 100%)}
  .gallery__photo--black{top:232px;height:200px;background:linear-gradient(135deg,#d6d8db 0%,#9fa4a9 55%,#e0e2e4 100%)}
  .gallery__caption{position:absolute;left:22px;top:232px;width:150px;height:200px;background:rgba(40,42,45,.88);color:var(--white);font-weight:700;font-size:12px;line-height:1.25;padding:40px 14px 0 16px}
</style>
</head>
<body>

<section class="spread spread--outer">
  <!-- back cover -->
  <article class="page page--back">
    <svg class="page__bg" viewBox="0 0 360 500" preserveAspectRatio="none" aria-hidden="true">
      <rect width="360" height="500" fill="#e4e4e4"/>
      <polygon points="0,0 360,0 360,330 0,262" fill="#2b2d30"/>
      <polygon points="0,262 360,330 360,500 0,500" fill="#2fae3e"/>
      <polygon points="0,352 360,312 360,500 0,500" fill="#e4e4e4"/>
    </svg>
    <div class="about">
      <h2 class="about__title">About Us</h2>
      <div class="about__rule"></div>
      <div class="about__cols">
        <div class="about__col">
          <p>Verdant Lab Works is a maker of laboratory service fittings, chemical resistant pipes, safety showers and eyewash units, fume cupboards and laboratory furniture. We are a reliable and trusted supplier for science spaces.</p>
          <p>Founded in 2005, we aim to be the one stop centre for laboratory engineering supplies, offering quality assurance and fair pricing.</p>
          <p>We supply service fittings, resistant piping, fume cupboards and emergency showers to contractors and builders, and export our products to the UAE, India and Asia.</p>
        </div>
        <div class="about__col">
          <p>Since its founding, the company has supplied a wide range of chemical resistant plumbing systems to schools, universities, hospitals and many government projects. Our emergency shower and eyewash units are made from stainless steel and certified to recognised standards. Quality is our main priority, and we carry trusted brands for plumbing systems, fittings and emergency showers.</p>
        </div>
      </div>
    </div>
    <h2 class="contact__title">Contact Us</h2>
    <p class="contact__company">Verdant Lab Works Sdn Bhd</p>
    <address class="contact__address" style="font-style:normal">
      <svg width="7" height="9" viewBox="0 0 7 9"><path d="M3.5 0a3 3 0 0 1 3 3c0 2.2-3 6-3 6S.5 5.2.5 3a3 3 0 0 1 3-3z" fill="#2fae3e"/><circle cx="3.5" cy="3" r="1.1" fill="#fff"/></svg>No. 12, Jalan Cempaka 7/3,<br>Section 7,<br>40000 Shah Alam,<br>Selangor,<br>MALAYSIA.
    </address>
    <div class="contact__logo brand"><span class="brand__mark"></span>Verdant Lab</div>
    <ul class="contact__lines">
      <li><svg width="8" height="8" viewBox="0 0 8 8"><circle cx="4" cy="4" r="3.4" fill="none" stroke="#2fae3e"/><path d="M2.6 2.4l.8-.3.6 1.1-.5.4c.3.6.6.9 1.2 1.2l.4-.5 1.1.6-.3.8c-1.8-.1-3.2-1.5-3.3-3.3z" fill="#2fae3e"/></svg>+60 3-5550 0142</li>
      <li><svg width="8" height="8" viewBox="0 0 8 8"><rect x=".5" y="1.5" width="7" height="5" fill="none" stroke="#2fae3e"/><path d="M.5 1.5L4 4.5l3.5-3" fill="none" stroke="#2fae3e"/></svg>hello@verdantlab.example</li>
      <li><svg width="8" height="8" viewBox="0 0 8 8"><circle cx="4" cy="4" r="3.4" fill="none" stroke="#2fae3e"/><path d="M.6 4h6.8M4 .6c-2 2-2 4.8 0 6.8M4 .6c2 2 2 4.8 0 6.8" fill="none" stroke="#2fae3e" stroke-width=".7"/></svg>www.verdantlab.example</li>
    </ul>
  </article>

  <!-- front cover -->
  <article class="page page--front">
    <svg class="page__bg" viewBox="0 0 360 500" preserveAspectRatio="none" aria-hidden="true">
      <rect width="360" height="500" fill="#e4e4e4"/>
    </svg>
    <div role="img" aria-label="Photo of a bright laboratory with ceramic worktop benches, microscopes, glass flasks and blue lab chairs" style="position:absolute;left:0;top:0;width:360px;height:340px;background:linear-gradient(160deg,#eceef0 0%,#cfd4d8 45%,#8f979e 100%)"></div>
    <svg class="page__bg" viewBox="0 0 360 500" preserveAspectRatio="none" aria-hidden="true">
      <path d="M0,250 L360,320 L360,418 Q180,400 0,392 Z" fill="#2fae3e"/>
    </svg>
    <h1 class="cover__title">
      <span class="cover__light">ceramic</span>
      <span class="cover__bold">worktop for</span>
      <span class="cover__light">laboratory</span>
      <span class="cover__sub">chemical resistant</span>
    </h1>
    <p class="cover__web">www.<b>verdantlab</b>.example</p>
    <div class="cover__logo brand"><span class="brand__mark"></span>Verdant Lab</div>
  </article>
</section>

<section class="spread spread--inner">
  <!-- product page -->
  <article class="page page--product">
    <svg class="page__bg" viewBox="0 0 360 500" preserveAspectRatio="none" aria-hidden="true">
      <rect width="360" height="500" fill="#f4f4f4"/>
      <polygon points="0,240 80,300 0,360" fill="#e6e6e6"/>
      <polygon points="300,380 360,330 360,450" fill="#e6e6e6"/>
    </svg>
    <header class="product__band">
      <div class="product__band-inner">
        <span class="product__code">CERA-V</span>
        <span class="product__name">LABORATORY CERAMIC WORKTOP</span>
      </div>
    </header>
    <ul class="features">
      <li class="feature"><svg class="feature__icon" viewBox="0 0 34 34"><circle cx="17" cy="17" r="16" fill="#e2531c"/><path d="M12 10h10v4l-3 2v8h-4v-8l-3-2z" fill="none" stroke="#fff" stroke-width="1.4"/></svg>Corrosion<br>Resistant</li>
      <li class="feature"><svg class="feature__icon" viewBox="0 0 34 34"><circle cx="17" cy="17" r="16" fill="#e2531c"/><path d="M10 24l14-14M13 24l11-11M10 21l11-11" stroke="#fff" stroke-width="1.4"/></svg>Scratch<br>Resistant</li>
      <li class="feature"><svg class="feature__icon" viewBox="0 0 34 34"><circle cx="17" cy="17" r="16" fill="#e2531c"/><path d="M17 8c1 4 6 6 6 11a6 6 0 0 1-12 0c0-3 2-4 3-6 0 2 1 3 2 3 0-3 0-5 1-8z" fill="none" stroke="#fff" stroke-width="1.4"/></svg>Fireproof<br>up to 1200 °C</li>
      <li class="feature"><svg class="feature__icon" viewBox="0 0 34 34"><circle cx="17" cy="17" r="16" fill="#e2531c"/><path d="M17 8l7 3v6c0 4-3 7-7 9-4-2-7-5-7-9v-6z" fill="none" stroke="#fff" stroke-width="1.4"/><path d="M14 17l2 2 4-4" fill="none" stroke="#fff" stroke-width="1.4"/></svg>Antibacterial</li>
      <li class="feature"><svg class="feature__icon" viewBox="0 0 34 34"><circle cx="17" cy="17" r="16" fill="#e2531c"/><path d="M10 10h14v14H10zM10 17h14M17 10v14" fill="none" stroke="#fff" stroke-width="1.4"/></svg>Non-<br>deformation</li>
      <li class="feature"><svg class="feature__icon" viewBox="0 0 34 34"><circle cx="17" cy="17" r="16" fill="#e2531c"/><path d="M11 22c3 0 4-3 6-3s3 3 6 3M14 11l1 2 2 1-2 1-1 2-1-2-2-1 2-1zM21 9l.6 1.4 1.4.6-1.4.6L21 13l-.6-1.4L19 11l1.4-.6z" fill="none" stroke="#fff" stroke-width="1.3"/></svg>Easy to<br>clean</li>
      <li class="feature"><svg class="feature__icon" viewBox="0 0 34 34"><circle cx="17" cy="17" r="16" fill="#e2531c"/><circle cx="17" cy="17" r="8" fill="none" stroke="#fff" stroke-width="1.4"/><path d="M11 11l12 12" stroke="#fff" stroke-width="1.4"/></svg>Non-inflammable<br>Class 1A</li>
      <li class="feature"><svg class="feature__icon" viewBox="0 0 34 34"><circle cx="17" cy="17" r="16" fill="#e2531c"/><path d="M17 8c3 5 6 8 6 12a6 6 0 0 1-12 0c0-4 3-7 6-12z" fill="none" stroke="#fff" stroke-width="1.4"/></svg>Waterproof</li>
    </ul>
    <div class="swatches">
      <div class="swatch"><span class="swatch__tab">WHITE</span><span class="swatch__chip swatch__chip--white"></span></div>
      <div class="swatch"><span class="swatch__tab">GREY</span><span class="swatch__chip swatch__chip--grey"></span></div>
      <div class="swatch"><span class="swatch__tab">BLACK</span><span class="swatch__chip swatch__chip--black"></span></div>
    </div>
    <div class="size-bar">AVAILABLE IN 2600 X 800 X 15MM</div>
    <p class="product__text">CERA-V laboratory 15mm ceramic worktops are sintered at a high temperature of 1200 °C and achieve the same colour through body and glaze, avoiding problems such as delamination and shedding. The ceramic worktop is corrosion-resistant, fireproof, waterproof, scratch resistant, abrasion resistant and free of deformation. Ceramic worktops resist strong acid, alkaline and organic solvent corrosion (except for hydrofluoric acid and equivalent chemical reagents).</p>
    <footer class="footer">
      <span class="footer__web">www.<b>verdantlab</b>.example</span>
      <span class="footer__rule"></span>
      <span class="brand brand--small"><span class="brand__mark"></span>Verdant Lab</span>
    </footer>
  </article>

  <!-- gallery page -->
  <article class="page page--gallery">
    <svg class="page__bg" viewBox="0 0 360 500" preserveAspectRatio="none" aria-hidden="true">
      <rect width="360" height="500" fill="#f4f4f4"/>
      <polygon points="0,380 40,420 0,460" fill="#e6e6e6"/>
    </svg>
    <div class="gallery__photo gallery__photo--white" role="img" aria-label="Photo of a laboratory room with white ceramic worktop benches and reagent shelves"></div>
    <div class="gallery__photo gallery__photo--black" role="img" aria-label="Photo of a laboratory work bench with a black ceramic worktop and white cabinets"></div>
    <p class="gallery__caption">Laboratory work bench with Black and Grey colour ceramic worktop</p>
    <footer class="footer">
      <span class="footer__web">www.<b>verdantlab</b>.example</span>
      <span class="footer__rule"></span>
      <span class="brand brand--small"><span class="brand__mark"></span>Verdant Lab</span>
    </footer>
  </article>
</section>

</body>
</html>
```